Hotel Business Card Project

Amber Crest Hotel will be a premium boutique hotel in Dhaka, Bangladesh. The hotel will offer the finest amenities and facilities available on the market, and the cost per room investment will far exceed other 5-star hotels currently in the market.

As a result, we wanted the business card to reflect that premium/luxurious/upscale feel, and also be elegant and hospitable at the same time.

The name 'Amber Crest' is derived from the fact that Bangladesh has 6 distinct seasons (you can get more information online if required, or contact me about it). The leaves in the logo has the tree because trees give people shade, protection and safety (just like our hotel would try to give).

Target Market(s)

Business professionals, guests

Industry/Entity Type

Investment

Requirements
Must have
• Elegant, Classy and very attractive business card.

Must be editable to enter specific Names, Positions, Phone numbers and email later on.
Nice to have
• The address would be: House 42, Road 57, Banani 4, Dhaka 1230, Bangladesh

Slogan- Luxury Redefined

```html
<!DOCTYPE html>
<html lang="en">
<head>
<meta charset="utf-8">
<title>Amber Crest Hotel – Business Cards</title>
<link href="https://fonts.googleapis.com/css2?family=Marcellus&family=Open+Sans:wght@400;600;700&display=swap" rel="stylesheet">
<style>
  :root {
    --stage: #7b3d1d;
    --paper: #ffffff;
    --espresso: #3b2b22;
    --ink: #2b211c;
    --slate: #6d6e71;
    --mark-grey: #6b6b6b;
    --amber: #c98a3c;
    --pattern-tone: #ece9e4;
  }
  * { margin: 0; padding: 0; box-sizing: border-box; }
  html, body { width: 1200px; height: 558px; overflow: hidden; }
  body {
    background: var(--stage);
    position: relative;
    font-family: "Open Sans", Arial, sans-serif;
    color: var(--ink);
  }
  .card {
    position: absolute;
    width: 339px;
    height: 193px;
    background: var(--paper);
    overflow: hidden;
  }
  .card--dark { background: var(--espresso); color: var(--paper); }

  .front { left: 190px; top: 56px; }
  .back-light { left: 562px; top: 56px; }
  .back-dark-reflect { left: 48px; top: 294px; }
  .back-dark { left: 430px; top: 294px; }
  .back-pattern { left: 812px; top: 298px; }

  /* brand name set as text */
  .brand {
    position: absolute;
    font-family: "Marcellus", Georgia, serif;
    font-weight: 400;
    color: var(--mark-grey);
    text-align: center;
    line-height: 1;
  }
  .brand__dot {
    position: absolute;
    border-radius: 50%;
    background: var(--amber);
  }
  .card--dark .brand { color: var(--paper); }
  .card--dark .brand__dot { background: var(--paper); }

  .front .brand__dot { left: 82px; top: 38px; width: 30px; height: 30px; }
  .front .brand { left: 20px; top: 114px; width: 155px; font-size: 21px; }
  .front .brand small { display: block; font-size: 8px; letter-spacing: 2px; margin-top: 3px; }

  .front .divider {
    position: absolute; left: 187px; top: 33px; width: 3px; height: 24px;
    background: var(--espresso);
  }
  .front .person { position: absolute; left: 198px; top: 34px; }
  .person__name { font-size: 12.5px; font-weight: 700; line-height: 1.1; }
  .person__title { font-size: 8px; }
  .contact {
    position: absolute; left: 198px; top: 67px;
    list-style: none; font-size: 8.5px; line-height: 10.6px;
  }
  .contact li { display: flex; align-items: center; gap: 4px; }
  .contact svg { width: 7px; height: 7px; flex: none; fill: var(--ink); }
  .address {
    position: absolute; left: 198px; top: 116px;
    font-size: 8.5px; line-height: 11px; display: flex; gap: 4px;
  }
  .address svg { width: 7px; height: 7px; margin-top: 2px; fill: var(--ink); flex: none; }

  .band-dark {
    position: absolute; left: 0; top: 174px; width: 185px; height: 19px;
    background: var(--espresso);
  }
  .band-slate {
    position: absolute; left: 190px; top: 174px; width: 149px; height: 19px;
    background: var(--slate);
  }
  .web {
    position: absolute; font-size: 10px; font-weight: 700;
    letter-spacing: 2.4px; text-align: center; white-space: nowrap;
  }
  .band-slate .web { position: static; color: var(--paper); font-size: 8px; letter-spacing: 1.8px; line-height: 19px; }

  .back-light .brand__dot { left: 152px; top: 28px; width: 36px; height: 36px; }
  .back-light .brand { left: 0; top: 92px; width: 339px; font-size: 28px; }
  .back-light .web { left: 0; width: 339px; top: 169px; color: var(--ink); font-size: 11px; }

  .back-dark-reflect .brand__dot { left: 152px; top: 36px; width: 36px; height: 36px; }
  .back-dark-reflect .brand { left: 0; top: 96px; width: 339px; font-size: 28px; }
  .back-dark-reflect .web { left: 0; width: 339px; top: 157px; color: var(--paper); }

  .back-dark .brand__dot { left: 152px; top: 46px; width: 36px; height: 36px; }
  .back-dark .brand { left: 0; top: 106px; width: 339px; font-size: 28px; }

  .pattern-field {
    position: absolute; inset: 0;
    background: linear-gradient(180deg, var(--pattern-tone), #f6f4f1 50%, var(--pattern-tone));
  }
  .back-pattern .brand {
    left: 0; top: 70px; width: 339px; font-size: 32px; color: var(--mark-grey);
  }
  .back-pattern .rule {
    position: absolute; top: 112px; height: 1px; width: 95px; background: var(--mark-grey);
  }
  .back-pattern .rule--left { left: 48px; }
  .back-pattern .rule--right { right: 48px; }
  .back-pattern .sub {
    position: absolute; left: 0; width: 339px; top: 106px; text-align: center;
    font-family: "Marcellus", Georgia, serif; font-size: 11px; letter-spacing: 2px;
    color: var(--mark-grey);
  }
  .back-pattern .web { left: 0; width: 339px; top: 161px; color: var(--ink); font-size: 11px; }
</style>
</head>
<body>

  <section class="card front" aria-label="Card front">
    <span class="brand__dot"></span>
    <div class="brand">AMBER CREST<small>HOTEL</small></div>
    <span class="divider"></span>
    <div class="person">
      <div class="person__name">Your Name</div>
      <div class="person__title">Title</div>
    </div>
    <ul class="contact">
      <li><svg viewBox="0 0 10 10"><path d="M2 0l2 2-1 2 3 3 2-1 2 2-2 2C4 10 0 6 0 2z"/></svg>123-456-7890</li>
      <li><svg viewBox="0 0 10 10"><rect x="2.5" y="0" width="5" height="10" rx="1"/></svg>456-789-1230</li>
      <li><svg viewBox="0 0 10 10"><rect x="2" y="0" width="6" height="3"/><rect x="0" y="3" width="10" height="5" rx="1"/><rect x="2" y="7" width="6" height="3"/></svg>789-123-4560</li>
      <li><svg viewBox="0 0 10 10"><path d="M0 2h10v6H0z M0 2l5 3 5-3" /></svg>info@ambercrest.com</li>
    </ul>
    <div class="address">
      <svg viewBox="0 0 10 10"><circle cx="5" cy="5" r="5"/></svg>
      <span>House 42, Road 57, Banani 4<br>Dhaka 1230, Bangladesh</span>
    </div>
    <div class="band-dark"></div>
    <div class="band-slate"><div class="web">www.ambercrest.com</div></div>
  </section>

  <section class="card back-light" aria-label="Card back, light">
    <span class="brand__dot"></span>
    <div class="brand">AMBER CREST</div>
    <div class="web">www.ambercrest.com</div>
  </section>

  <section class="card card--dark back-dark-reflect" aria-label="Card back, dark with web address">
    <span class="brand__dot"></span>
    <div class="brand">AMBER CREST</div>
    <div class="web">www.ambercrest.com</div>
  </section>

  <section class="card card--dark back-dark" aria-label="Card back, dark">
    <span class="brand__dot"></span>
    <div class="brand">AMBER CREST</div>
  </section>

  <section class="card back-pattern" aria-label="Card back, patterned">
    <div class="pattern-field" role="img" aria-label="Faint repeating brand pattern background"></div>
    <div class="brand">AMBER CREST</div>
    <span class="rule rule--left"></span>
    <span class="rule rule--right"></span>
    <div class="sub">HOTEL</div>
    <div class="web">www.ambercrest.com</div>
  </section>

</body>
</html>
```